Invitation - Melbourne Show Invitation

We need an e-Invitation for our Trade Show in Melbourne. We are holding a furniture show at our Melbourne Showroom:

The Harbourline Private Show

Dates: Wednesday 19th to Friday 21st July

Hours: 9am to 6pm

Join us for Drinks on Thursday 20th from 5pm

Address:
The Lantern Loft
47 Arden Lane
Melbourne

RSVP: rosalind@harbourline-au.example

Tel. 03 9555 0172

The style of the building and the furniture is mid-century design, so I would like the invitation to reflect this (think "Tin Hats").

Target Market(s)

Professional Retailers

Industry/Entity Type

Trade

Font styles to use
Sans Serif

Colors

Designer to choose colors to be used in the design.

Requirements
Must have
• Dates and Times

```html
<!DOCTYPE html>
<html lang="en">
<head>
<meta charset="utf-8">
<title>The Harbourline Private Show – Invitation</title>
<link rel="stylesheet" href="https://fonts.googleapis.com/css2?family=Montserrat:wght@400;600;700;800&family=Questrial&family=Oswald:wght@300;400&display=swap">
<style>
  :root {
    --paper: #f1e4cd;
    --paper-edge: #e6cfa8;
    --frame: #c99a63;
    --ornament: #d9ad74;
    --wine: #8a1515;
    --ink: #2a2522;
    --band: #3b2519;
    --navy: #1d2442;
    --sofa: #c48f55;
    --sofa-light: #d6a86f;
    --white: #fffaf0;
  }
  * { margin: 0; padding: 0; box-sizing: border-box; }
  html, body { width: 950px; height: 1200px; overflow: hidden; background: #ece8e2; }
  .invitation {
    position: relative;
    width: 950px;
    height: 1200px;
    overflow: hidden;
    background: radial-gradient(ellipse at 50% 45%, var(--paper) 55%, var(--paper-edge) 100%);
    font-family: "Montserrat", sans-serif;
    color: var(--ink);
  }
  .abs { position: absolute; }
  .inner-frame { left: 64px; top: 60px; width: 812px; height: 1118px; border: 1px solid var(--frame); opacity: .7; }

  .ornament-corner { left: 552px; top: 40px; width: 353px; height: 324px; border-radius: 0 0 0 100%; background: radial-gradient(circle at 80% 20%, rgba(217,173,116,.45), rgba(217,173,116,0) 70%); }
  .ornament-swirl { left: 46px; top: 691px; width: 133px; height: 354px; border-radius: 60px; background: linear-gradient(180deg, rgba(217,173,116,0), rgba(217,173,116,.35) 50%, rgba(217,173,116,0)); }
  .chair-motif { left: 581px; top: 718px; width: 359px; height: 482px; border-radius: 160px 160px 0 0; background: linear-gradient(180deg, rgba(201,154,99,.18), rgba(201,154,99,.08)); }
  .chaise-shape { left: 36px; top: 975px; width: 457px; height: 225px; border-radius: 70px 40px 0 0; background: linear-gradient(180deg, var(--sofa-light), var(--sofa)); }

  .title { left: 160px; top: 140px; }
  .title text { font-family: "Montserrat", sans-serif; font-weight: 800; }

  .show-band { left: 174px; top: 454px; width: 594px; height: 51px; background: var(--band); color: var(--white); font-family: "Questrial", sans-serif; font-size: 40px; letter-spacing: 3px; text-align: center; line-height: 51px; }

  .dates { left: 174px; top: 550px; width: 250px; height: 280px; }
  .dates > * { position: absolute; white-space: nowrap; }
  .day-name { left: 0; font-family: "Questrial", sans-serif; color: var(--ink); line-height: 1; }
  .day-wed { top: 0; font-size: 31px; letter-spacing: 2.5px; }
  .day-fri { top: 122px; font-size: 40px; letter-spacing: 9px; }
  .day-num { left: 0; font-weight: 800; font-size: 112px; line-height: 1; letter-spacing: -5px; color: var(--ink); }
  .num-19 { top: 24px; }
  .num-21 { top: 156px; }
  .suffix { left: 124px; width: 116px; text-align: center; font-weight: 700; font-size: 52px; line-height: 1; color: var(--ink); }
  .suffix-th { top: 36px; }
  .suffix-st { top: 168px; }
  .tag { left: 124px; width: 116px; height: 30px; background: var(--wine); color: var(--white); font-weight: 800; text-align: center; line-height: 30px; }
  .tag-to { top: 82px; font-size: 26px; }
  .tag-july { top: 214px; font-size: 22px; letter-spacing: 1px; }
  .hours { top: 256px; left: 12px; font-weight: 800; font-size: 26px; letter-spacing: 1px; color: var(--navy); line-height: 1; }

  .divider { left: 449px; top: 550px; width: 0; height: 262px; border-left: 1px solid var(--frame); }

  .drinks-box { left: 491px; top: 564px; width: 285px; height: 247px; border: 1px dashed var(--frame); border-radius: 10px; }
  .drinks-box > * { position: absolute; white-space: nowrap; line-height: 1; }
  .drinks-box .join { top: 14px; right: 16px; font-family: "Questrial", sans-serif; font-size: 21px; letter-spacing: 1px; }
  .drinks-box .drinks { top: 40px; right: 16px; font-weight: 800; font-size: 46px; color: var(--wine); letter-spacing: 2px; }
  .drinks-box .thursday { top: 92px; left: 18px; font-family: "Questrial", sans-serif; font-size: 27px; letter-spacing: 1px; }
  .drinks-box .big-20 { top: 118px; left: 18px; font-weight: 800; font-size: 92px; letter-spacing: -4px; }
  .drinks-box .suffix-20 { top: 126px; left: 150px; font-weight: 700; font-size: 48px; }
  .drinks-box .from { top: 200px; left: 20px; font-family: "Questrial", sans-serif; font-size: 34px; letter-spacing: 2px; }
  .drinks-box .from strong { font-family: "Montserrat", sans-serif; font-weight: 700; color: var(--navy); font-size: 32px; letter-spacing: 1px; }

  .venue { left: 164px; top: 872px; }
  .venue svg { position: absolute; left: 0; top: 8px; }
  .venue-text { position: absolute; left: 71px; top: 0; width: 600px; font-weight: 600; font-size: 25px; line-height: 29px; letter-spacing: .5px; color: var(--band); }

  .rsvp { left: 100px; top: 1030px; font-family: "Oswald", sans-serif; font-weight: 300; color: var(--ink); }
  .rsvp-label { position: absolute; left: 32px; top: 0; font-size: 30px; color: var(--white); }
  .rsvp-row { position: absolute; left: 0; display: flex; align-items: center; gap: 12px; white-space: nowrap; font-size: 24px; font-weight: 400; }
  .rsvp-mail { top: 56px; }
  .rsvp-phone { top: 92px; font-size: 30px; }
  .rsvp-icon { width: 22px; height: 22px; border-radius: 50%; background: var(--white); display: flex; align-items: center; justify-content: center; }

  .brand { left: 515px; top: 1093px; display: flex; align-items: center; gap: 18px; }
  .brand-square { width: 54px; height: 54px; background: var(--ink); border-radius: 8px; }
  .brand-name { font-weight: 700; font-size: 44px; color: var(--ink); letter-spacing: -1px; }
</style>
</head>
<body>
<main class="invitation">
  <div class="abs ornament-corner" role="img" aria-label="Decorative flourish ornament in gold"></div>
  <div class="abs ornament-swirl" role="img" aria-label="Decorative swirling scroll ornament in gold"></div>
  <div class="abs chair-motif" role="img" aria-label="Faint outline of a mid-century armchair"></div>
  <div class="abs inner-frame"></div>

  <svg class="abs title" width="620" height="310" viewBox="0 0 620 310" aria-label="The Harbourline">
    <text transform="translate(113 166) rotate(-90)" font-size="130" fill="var(--ink)" textLength="155" lengthAdjust="spacingAndGlyphs">THE</text>
    <text x="117" y="152" font-size="130" fill="var(--wine)" textLength="493" lengthAdjust="spacingAndGlyphs">HARBOUR</text>
    <text x="9" y="294" font-size="172" fill="var(--ink)" textLength="599" lengthAdjust="spacingAndGlyphs">LINE</text>
  </svg>

  <div class="abs show-band">PRIVATE SHOW</div>

  <section class="abs dates">
    <div class="day-name day-wed">WEDNESDAY</div>
    <div class="day-num num-19">19</div>
    <div class="suffix suffix-th">TH</div>
    <div class="tag tag-to">TO</div>
    <div class="day-name day-fri">FRIDAY</div>
    <div class="day-num num-21">21</div>
    <div class="suffix suffix-st">ST</div>
    <div class="tag tag-july">JULY</div>
    <div class="hours">9AM TO 6PM</div>
  </section>

  <div class="abs divider"></div>

  <section class="abs drinks-box">
    <div class="join">JOIN US FOR</div>
    <div class="drinks">DRINKS</div>
    <div class="thursday">ON THURSDAY</div>
    <div class="big-20">20</div>
    <div class="suffix-20">TH</div>
    <div class="from">FROM <strong>5PM</strong></div>
  </section>

  <section class="abs venue">
    <svg width="42" height="50" viewBox="0 0 42 50" aria-hidden="true">
      <path d="M21 2C11 2 4 9.5 4 19c0 12 17 29 17 29s17-17 17-29C38 9.5 31 2 21 2z" fill="var(--ink)"/>
      <circle cx="21" cy="19" r="6.5" fill="var(--paper)"/>
    </svg>
    <div class="venue-text">THE LANTERN LOFT, 47 ARDEN LANE<br>MELBOURNE</div>
  </section>

  <div class="abs chaise-shape" role="img" aria-label="Illustration of a mid-century chaise longue in tan"></div>

  <section class="abs rsvp">
    <div class="rsvp-label">RSVP:</div>
    <div class="rsvp-row rsvp-mail">
      <span class="rsvp-icon"><svg width="12" height="9" viewBox="0 0 12 9"><rect x=".5" y=".5" width="11" height="8" fill="none" stroke="var(--sofa)"/><path d="M.5 .5L6 5l5.5-4.5" fill="none" stroke="var(--sofa)"/></svg></span>
      <span>rosalind@harbourline-au.example</span>
    </div>
    <div class="rsvp-row rsvp-phone">
      <span class="rsvp-icon"><svg width="12" height="12" viewBox="0 0 12 12"><path d="M2.5 1l2 2.2-1 1.3c.8 1.6 2 2.8 3.6 3.6l1.3-1 2.2 2-1.3 1.7C5 10.5 1.5 7 .8 2.3z" fill="var(--sofa)"/></svg></span>
      <span>03 9555 0172</span>
    </div>
  </section>

  <div class="abs brand">
    <span class="brand-square"></span>
    <span class="brand-name">Harbourline</span>
  </div>
</main>
</body>
</html>
```